Business Card Design

Looking for a professional looking business card for a carpentry/construction business that deals with renovations, extensions, homes, and anything carpentry based in Northern Australia. Would like to incorporate the attached logo with backgrounds of white, grey or maybe a close up of timber/wood grain. Thanks

Industry/Entity Type

Carpentry

Contact Information for Business Card

Dean Carlow, Owner, Po Box 2674 Katherine NT 0851, dean-carlow@fernmail.example, 0419563072, Builders Number: 293417CR

Requirements
Should not have
• Power tools/hand tools related to carpentry

```html
<!DOCTYPE html>
<html lang="en">
<head>
<meta charset="utf-8">
<title>Carlow Carpentry – Business Card</title>
<link rel="stylesheet" href="https://fonts.googleapis.com/css2?family=Arimo:wght@400;700&family=Arvo:wght@700&display=swap">
<style>
  :root {
    --wood-light: #e3b07e;
    --wood-mid: #d49a63;
    --wood-dark: #c3834c;
    --panel: rgba(255, 246, 236, 0.55);
    --sign-wood: #c98f5c;
    --sign-frame: #7a4a28;
    --brand-blue: #1f4fa8;
    --ink-brown: #3a2414;
    --ink-dark: #2f1d10;
  }
  html, body {
    margin: 0;
    padding: 0;
    overflow: hidden;
    background: #ffffff;
  }
  .card {
    position: relative;
    width: 1200px;
    height: 741px;
    overflow: hidden;
  }
  .card__timber {
    position: absolute;
    inset: 0;
    background: linear-gradient(135deg, var(--wood-light) 0%, var(--wood-mid) 50%, var(--wood-dark) 100%);
  }
  .card__panel {
    position: absolute;
    left: 108px;
    top: 99px;
    width: 982px;
    height: 547px;
    background: var(--panel);
  }
  .card__content {
    position: absolute;
    left: 0;
    width: 1152px;
    text-align: center;
  }
  .builders-number {
    top: 100px;
    font: 400 40px/1 "Arimo", sans-serif;
    color: var(--ink-dark);
    letter-spacing: 0.5px;
  }
  .brand-sign {
    position: absolute;
    left: 344px;
    top: 148px;
    width: 461px;
    height: 165px;
    box-sizing: border-box;
    background: var(--sign-wood);
    border: 5px solid var(--sign-frame);
    display: flex;
    align-items: center;
    justify-content: center;
  }
  .brand-sign__name {
    font: 700 54px/1 "Arimo", sans-serif;
    color: var(--brand-blue);
  }
  .owner-name {
    top: 318px;
    font: 700 66px/1 "Arvo", serif;
    color: var(--ink-brown);
  }
  .owner-role {
    top: 400px;
    font: 700 42px/1 "Arvo", serif;
    color: var(--ink-brown);
  }
  .contact-line {
    font: 700 35px/1 "Arimo", sans-serif;
    color: var(--ink-brown);
  }
  .contact-line--address { top: 468px; }
  .contact-line--email { top: 535px; }
  .contact-line--phone { top: 598px; }
</style>
</head>
<body>
  <div class="card">
    <div class="card__timber" role="img" aria-label="Close-up timber plank wall with wood grain and nail heads"></div>
    <div class="card__panel"></div>

    <div class="card__content builders-number">Builders Number: 293417CR</div>

    <div class="brand-sign">
      <span class="brand-sign__name">Carlow Carpentry</span>
    </div>

    <div class="card__content owner-name">Dean Carlow</div>
    <div class="card__content owner-role">(OWNER)</div>

    <div class="card__content contact-line contact-line--address">P.O. Box :2674, Katherine NT 0851,</div>
    <div class="card__content contact-line contact-line--email">E-mail : dean-carlow@fernmail.example,</div>
    <div class="card__content contact-line contact-line--phone">Contact No. : 0419563072</div>
  </div>
</body>
</html>
```